Design Business Card for HollenAdvisoryPartners

Design business cards for my Consulting Firm; The end result will be uploaded into LumbraCards for ordering of business cards

```html
<!DOCTYPE html>
<html lang="en">
<head>
<meta charset="utf-8">
<title>HollenAdvisoryPartners Business Card</title>
<link rel="stylesheet" href="https://fonts.googleapis.com/css2?family=Lato:wght@400;700&display=swap">
<style>
  :root {
    --bg: #ecebe8;
    --card: #ffffff;
    --ink: #3a3a3a;
    --ink-soft: #5a5a5a;
    --accent: #d9262c;
    --neutral: #b5b5b5;
    --shadow: rgba(0,0,0,0.18);
  }
  * { box-sizing: border-box; margin: 0; padding: 0; }
  html, body { width: 1200px; height: 911px; overflow: hidden; }
  body { background: var(--bg); position: relative; font-family: "Lato", sans-serif; color: var(--ink); }

  .card {
    position: absolute;
    width: 600px; height: 343px;
    background: var(--card);
    box-shadow: 0 6px 18px var(--shadow);
  }
  .card--front { left: 60px; top: 70px; }
  .card--back { left: 540px; top: 498px; }

  .brand { position: absolute; display: flex; align-items: center; gap: 12px; }
  .brand__name { font-family: "Lato", sans-serif; font-weight: 400; color: var(--ink); }
  .brand__mark { background: var(--neutral); flex: none; }

  .card--front .brand { left: 48px; top: 146px; }
  .card--front .brand__name { font-size: 32px; }
  .card--front .brand__mark { width: 26px; height: 26px; }
  .front__web { position: absolute; right: 40px; bottom: 34px; font-size: 14px; color: var(--ink-soft); }

  .card--back .brand { left: 34px; top: 42px; }
  .card--back .brand__name { font-size: 18px; }
  .card--back .brand__mark { width: 16px; height: 16px; }

  .holder { position: absolute; right: 24px; top: 92px; text-align: right; }
  .holder__name { color: var(--accent); font-weight: 700; font-size: 16px; letter-spacing: 0.3px; }
  .holder__title { font-size: 12px; color: var(--ink-soft); margin-top: 2px; }
  .holder__company { font-size: 14px; font-weight: 700; color: var(--ink); margin-top: 1px; }
  .holder__bar { position: absolute; right: 0; top: 86px; width: 8px; height: 58px; background: var(--accent); }
  .address { position: absolute; right: 24px; top: 166px; font-size: 13px; color: var(--ink-soft); }

  .contact { position: absolute; left: 34px; bottom: 26px; list-style: none; }
  .contact__item { display: flex; align-items: center; gap: 9px; font-size: 14px; color: var(--ink); line-height: 22px; }
  .contact__icon { width: 13px; height: 13px; fill: var(--accent); flex: none; }
</style>
</head>
<body>
  <section class="card card--front">
    <div class="brand">
      <span class="brand__name">HollenAdvisoryPartners</span>
      <span class="brand__mark"></span>
    </div>
    <p class="front__web">www.HollenAdvisoryPartners.com</p>
  </section>

  <section class="card card--back">
    <div class="brand">
      <span class="brand__name">HollenAdvisoryPartners</span>
      <span class="brand__mark"></span>
    </div>

    <span class="holder__bar"></span>
    <div class="holder">
      <p class="holder__name">Daniel M. Corwin, PMP, CSM</p>
      <p class="holder__title">President / CEO</p>
      <p class="holder__company">HollenAdvisoryPartners</p>
    </div>
    <p class="address">Maplewood, LA 70000</p>

    <ul class="contact">
      <li class="contact__item">
        <svg class="contact__icon" viewBox="0 0 16 16"><path d="M3.5 1l3 3-2 2c1 2 3 4 5 5l2-2 3 3-2 3C7 14 2 9 1 3.5z"/></svg>
        555.010.4821
      </li>
      <li class="contact__item">
        <svg class="contact__icon" viewBox="0 0 16 16"><path d="M4 1h8v4H4z M1 6h14v7h-3v2H4v-2H1z M5 10v4h6v-4z"/></svg>
        555.010.7390
      </li>
      <li class="contact__item">
        <svg class="contact__icon" viewBox="0 0 16 16"><path d="M1 3h14v10H1z M1.5 3.5L8 9l6.5-5.5" fill="var(--accent)" stroke="#fff" stroke-width="1.2"/></svg>
        daniel.corwin@hollenadvisorypartners.com
      </li>
      <li class="contact__item">
        <svg class="contact__icon" viewBox="0 0 16 16"><circle cx="8" cy="8" r="7"/><path d="M1 8h14M8 1c-3 4-3 10 0 14M8 1c3 4 3 10 0 14" stroke="#fff" stroke-width="1" fill="none"/></svg>
        www.HollenAdvisoryPartners.com
      </li>
    </ul>
  </section>
</body>
</html>
```